Design a double sided business card

We are looking for a clean, eye-catching, and contemporary design that enhances the brand and presents a premium, professional image. Our preference is for a brown card with black gloss detailing and embossed elements; however, we are open to creative input and design suggestions that best achieve a strong visual impact.

Please see the attached existing business card for reference. We use both black and brown colours consistently across our branding.

On sample provided

```html
<!DOCTYPE html>
<html lang="en">
<head>
<meta charset="utf-8">
<title>Corvane – Business Card</title>
<link href="https://fonts.googleapis.com/css2?family=Montserrat:wght@400;600&display=swap" rel="stylesheet">
<style>
  :root {
    --ink: #000000;
    --tan: #c8b59b;
    --canvas: #e6e6e6;
    --rule: #1e1e1e;
  }
  * { margin: 0; padding: 0; box-sizing: border-box; }
  html, body {
    width: 1200px; height: 849px; overflow: hidden;
    background: var(--canvas);
    font-family: "Montserrat", sans-serif;
  }
  .sheet {
    position: relative; width: 1200px; height: 849px;
  }
  .card {
    position: absolute; left: 303px;
    width: 594px; height: 340px;
    overflow: hidden;
  }
  .card-front { top: 65px; background: var(--tan); }
  .card-back { top: 445px; background: var(--ink); }
  .card-shape { position: absolute; inset: 0; width: 100%; height: 100%; }

  /* Front */
  .front-rule {
    position: absolute; left: 148px; width: 297px; height: 1px;
    background: var(--rule);
  }
  .front-rule.top { top: 59px; }
  .front-rule.bottom { top: 283px; }
  .wordmark {
    position: absolute; left: 0; right: 0; top: 146px;
    display: flex; align-items: center; justify-content: center; gap: 14px;
    color: var(--tan);
  }
  .wordmark-square {
    width: 26px; height: 26px; background: var(--tan);
  }
  .wordmark-name {
    font-weight: 600; font-size: 40px; letter-spacing: 5px; line-height: 1;
  }

  /* Back */
  .holder {
    position: absolute; left: 31px; top: 28px; color: var(--tan);
  }
  .holder-name {
    font-weight: 600; font-size: 27px; line-height: 1.1;
    padding-bottom: 2px; border-bottom: 1.5px solid var(--tan);
    display: inline-block;
  }
  .holder-role {
    display: block; font-size: 12px; letter-spacing: 8.4px; margin-top: 3px;
  }
  .contacts {
    position: absolute; left: 29px; top: 110px; list-style: none;
    color: var(--tan); font-size: 15px; line-height: 1;
  }
  .contacts li {
    display: flex; align-items: flex-start; gap: 11px; height: 34px;
  }
  .contacts li.address { line-height: 1.65; margin-top: 2px; }
  .contact-icon { width: 19px; height: 19px; flex: none; margin-top: -1px; }
  .back-mark {
    position: absolute; right: 26px; top: 150px;
    color: var(--ink); font-weight: 600; font-size: 24px; letter-spacing: 3px;
  }
</style>
</head>
<body>
<main class="sheet">

  <section class="card card-front" aria-label="Card front">
    <svg class="card-shape" viewBox="0 0 688 394" preserveAspectRatio="none" aria-hidden="true">
      <path fill="var(--ink)" d="M110,0 H688 V170 C688,300 590,394 460,394 H0 V120 C0,50 50,0 110,0 Z"/>
    </svg>
    <span class="front-rule top"></span>
    <div class="wordmark">
      <span class="wordmark-square"></span>
      <span class="wordmark-name">CORVANE</span>
    </div>
    <span class="front-rule bottom"></span>
  </section>

  <section class="card card-back" aria-label="Card back">
    <svg class="card-shape" viewBox="0 0 688 394" preserveAspectRatio="none" aria-hidden="true">
      <path fill="var(--tan)" d="M440,0 C350,120 400,330 620,394 H688 V0 Z"/>
    </svg>

    <div class="holder">
      <span class="holder-name">Ravi Sandhu</span>
      <span class="holder-role">DIRECTOR</span>
    </div>

    <ul class="contacts">
      <li>
        <svg class="contact-icon" viewBox="0 0 20 20" aria-hidden="true">
          <circle cx="10" cy="10" r="10" fill="var(--tan)"/>
          <path fill="var(--ink)" d="M6.5,5 l2,0 l1,2.6 l-1.3,1 a6,6 0 0 0 3.2,3.2 l1,-1.3 l2.6,1 l0,2 a1,1 0 0 1 -1,1 A9,9 0 0 1 5.5,6 a1,1 0 0 1 1,-1 z"/>
        </svg>
        <span>0800 555 0142</span>
      </li>
      <li>
        <svg class="contact-icon" viewBox="0 0 20 20" aria-hidden="true">
          <circle cx="10" cy="10" r="10" fill="var(--tan)"/>
          <rect x="7" y="4.5" width="6" height="11" rx="1" fill="none" stroke="var(--ink)" stroke-width="1.4"/>
          <circle cx="10" cy="13.3" r="0.8" fill="var(--ink)"/>
        </svg>
        <span>07700900461</span>
      </li>
      <li>
        <svg class="contact-icon" viewBox="0 0 20 20" aria-hidden="true">
          <circle cx="10" cy="10" r="10" fill="var(--tan)"/>
          <rect x="5" y="6.5" width="10" height="7" fill="none" stroke="var(--ink)" stroke-width="1.3"/>
          <path d="M5,6.5 L10,10.5 L15,6.5" fill="none" stroke="var(--ink)" stroke-width="1.3"/>
        </svg>
        <span>ravi@corvane.co.uk</span>
      </li>
      <li>
        <svg class="contact-icon" viewBox="0 0 20 20" aria-hidden="true">
          <circle cx="10" cy="10" r="10" fill="var(--tan)"/>
          <g fill="none" stroke="var(--ink)" stroke-width="1.1">
            <circle cx="10" cy="10" r="5"/>
            <ellipse cx="10" cy="10" rx="2.2" ry="5"/>
            <path d="M5,10 H15 M6,7.5 H14 M6,12.5 H14"/>
          </g>
        </svg>
        <span>www.corvane.co.uk</span>
      </li>
      <li class="address">
        <svg class="contact-icon" viewBox="0 0 20 20" aria-hidden="true">
          <circle cx="10" cy="10" r="10" fill="var(--tan)"/>
          <path fill="var(--ink)" d="M10,4 a4,4 0 0 1 4,4 c0,3 -4,8 -4,8 c0,0 -4,-5 -4,-8 a4,4 0 0 1 4,-4 z"/>
          <circle cx="10" cy="8" r="1.5" fill="var(--tan)"/>
        </svg>
        <span>The Green Mill Lane<br>Harrowfield HF4 2QD</span>
      </li>
    </ul>

    <span class="back-mark">CORVANE</span>
  </section>

</main>
</body>
</html>
```